Business Cards For Glintwell
Desmond Kuvetti
Simple
CEO and Founder
2871 Pellfield Ln Brockville Ontario K3P2c8
Desmond@Kuvetti-mail.test
Keep it simple and clean. We want the logo BIG on the one side and company info on the other. If you can get some type of interlock going from bad to restored too that might look nice faded as a background on one of the sides.
750PineRidgeRnR 750PineRidgeRnR
https://www.socialpage.test/750PineRidgeRR/photos/pb.382915067214433.-1109384000.1285719304./517293048116520/?type=3&theater this is a good picture that would be nice to have one one side of the cards faded out
Logo has been uploaded.
Grafto Grafto
kindly upload logo

```html
<!DOCTYPE html>
<html lang="en">
<head>
<meta charset="utf-8">
<title>Glintwell Business Cards</title>
<link href="https://fonts.googleapis.com/css2?family=Roboto+Condensed:wght@400;700&display=swap" rel="stylesheet">
<style>
  :root {
    --backdrop: #e9e6e1;
    --card: #ffffff;
    --navy: #2d3a8a;
    --navy-dark: #232e70;
    --silver: #9c9fa5;
    --ink: #3a3d44;
    --on-navy: #ffffff;
  }
  * { margin: 0; padding: 0; box-sizing: border-box; }
  html, body { width: 1200px; height: 982px; overflow: hidden; }
  body {
    background: var(--backdrop);
    font-family: "Roboto Condensed", Arial, sans-serif;
    position: relative;
  }
  .card {
    position: absolute;
    background: var(--card);
    box-shadow: 0 6px 18px rgba(0,0,0,.18);
    overflow: hidden;
  }
  .card-info { left: 40px; top: 320px; width: 600px; height: 343px; }
  .card-logo { left: 720px; top: 191px; width: 343px; height: 600px; }

  .band { position: absolute; inset: 0; width: 100%; height: 100%; }

  .brand { position: absolute; color: var(--ink); }
  .brand-name {
    display: block;
    font-weight: 700;
    letter-spacing: .5px;
    line-height: 1;
  }
  .brand-tag {
    display: block;
    font-weight: 400;
    letter-spacing: 1.5px;
    line-height: 1;
    border-top: 2px solid var(--navy);
    padding-top: 5px;
    margin-top: 5px;
  }
  .card-info .brand { left: 38px; top: 118px; }
  .card-info .brand-name { font-size: 44px; }
  .card-info .brand-tag { font-size: 14.5px; }
  .card-logo .brand { left: 50%; top: 50%; transform: translate(-50%, -50%); text-align: left; }
  .card-logo .brand-name { font-size: 46px; }
  .card-logo .brand-tag { font-size: 15px; }

  .person { position: absolute; left: 38px; bottom: 38px; color: var(--navy); }
  .person-name { font-size: 17px; font-weight: 700; letter-spacing: 1.5px; text-transform: uppercase; }
  .person-role { font-size: 12px; letter-spacing: 2px; text-transform: uppercase; margin-top: 3px; }

  .contact { position: absolute; color: var(--on-navy); font-size: 12px; line-height: 1.35; }
  .contact-address { left: 352px; top: 70px; width: 210px; }
  .contact-list { left: 352px; top: 150px; list-style: none; }
  .contact-list li { display: flex; align-items: center; gap: 8px; margin-bottom: 9px; }
  .contact-list svg { width: 14px; height: 14px; flex: none; }
</style>
</head>
<body>

<section class="card card-info" aria-label="Business card, contact side">
  <svg class="band" viewBox="0 0 600 343" preserveAspectRatio="none" aria-hidden="true">
    <path d="M330 0 C300 110 290 230 245 343 L262 343 C306 230 316 110 346 0 Z" fill="var(--silver)"/>
    <path d="M352 0 C322 110 312 230 268 343 L600 343 L600 0 Z" fill="var(--navy)"/>
  </svg>

  <div class="brand">
    <span class="brand-name">GLINTWELL</span>
    <span class="brand-tag">CLEANING &amp; RESTORATION</span>
  </div>

  <div class="person">
    <div class="person-name">Desmond Kuvetti</div>
    <div class="person-role">CEO and Founder</div>
  </div>

  <address class="contact contact-address" style="font-style:normal">
    2871 Pellfield Ln<br>Brockville Ontario K3P2c8
  </address>

  <ul class="contact contact-list">
    <li>
      <svg viewBox="0 0 24 24" fill="var(--on-navy)" aria-hidden="true"><path d="M6.6 10.8a15.1 15.1 0 0 0 6.6 6.6l2.2-2.2c.3-.3.7-.4 1-.2 1.1.4 2.3.6 3.6.6.6 0 1 .4 1 1V20c0 .6-.4 1-1 1A17 17 0 0 1 3 4c0-.6.4-1 1-1h3.5c.6 0 1 .4 1 1 0 1.3.2 2.5.6 3.6.1.3 0 .7-.2 1z"/></svg>
      <span>+1 613 555 0142</span>
    </li>
    <li>
      <svg viewBox="0 0 24 24" fill="var(--on-navy)" aria-hidden="true"><path d="M3 5h18v14H3z M4 6l8 6 8-6" stroke="var(--navy)" stroke-width="1.5"/></svg>
      <span>Desmond@Kuvetti-mail.test</span>
    </li>
    <li>
      <svg viewBox="0 0 24 24" fill="none" stroke="var(--on-navy)" stroke-width="2" aria-hidden="true"><circle cx="12" cy="12" r="9"/><path d="M3 12h18M12 3c3 3 3 15 0 18M12 3c-3 3-3 15 0 18"/></svg>
      <span>www.glintwell.test</span>
    </li>
  </ul>
</section>

<section class="card card-logo" aria-label="Business card, logo side">
  <div class="brand">
    <span class="brand-name">GLINTWELL</span>
    <span class="brand-tag">CLEANING &amp; RESTORATION</span>
  </div>
</section>

</body>
</html>
```